Harvest Cellar

We need desigin for our main page(concept will be used for other pages also).
We already have a logo, and moqup of our main page(see attch).
You could change layers and positions on moqup, but please use logo, and its colors in design creating. (We have logo in different colors, i attached 2 samples, so you could use also another colors if you wish).

Our bussinees will be something similar to BloomLaunch or Seedwell.io, but with some special features. So main idea: start-ups, donations, investemnets

Designs were prefer:
http://seedwell.io/
http://www.bloomlaunch-example.com/

Brief was updated.

Target Market(s)

Clients are middle aged persons, who interested in new start-ups, investments and so on.

Requirements
Must have
• Design must be neat

```html
<!DOCTYPE html>
<html lang="en">
<head>
<meta charset="utf-8">
<title>Harvest Cellar</title>
<link rel="stylesheet" href="https://fonts.googleapis.com/css2?family=Arimo:wght@400;700&family=Roboto+Condensed:wght@400;700&family=Ubuntu:wght@400;500&display=swap">
<style>
:root{
  --navy:#1b4a86;
  --navy-dark:#123a6e;
  --navy-light:#2c66a8;
  --page:#e8e8e8;
  --panel:#f7f7f7;
  --line:#d4d4d4;
  --text:#333;
  --muted:#777;
  --lime:#a9c92a;
  --lime-dark:#86a81a;
  --sky:#3f8fdc;
  --footer:#1d5697;
  --footer-dark:#153f72;
}
*{box-sizing:border-box;margin:0;padding:0}
html,body{width:960px;height:1200px;overflow:hidden}
body{position:relative;background:var(--page);font-family:Arimo,Arial,sans-serif;color:var(--text)}
.abs{position:absolute}
/* header */
.header{left:0;top:0;width:960px;height:113px;background:linear-gradient(#fbfbfb,#ececec);border-bottom:2px solid #d6d6d6}
.brand{left:96px;top:44px;display:flex;align-items:center;gap:6px}
.brand-mark{width:22px;height:22px;border-radius:50%;background:var(--navy)}
.brand-name{font-family:"Roboto Condensed",sans-serif;font-weight:700;font-size:22px;color:var(--navy);letter-spacing:.5px}
.nav-btn{top:67px;width:90px;height:28px;background:linear-gradient(#2a64a6,var(--navy-dark));border-radius:5px;color:#fff;font-size:10px;text-align:center;line-height:28px}
.nav-btn::after{content:"";position:absolute;left:39px;bottom:-7px;border:6px solid transparent;border-top:7px solid var(--navy-dark);border-bottom:0}
.search{left:702px;top:14px;width:176px;height:30px;border-radius:15px;background:linear-gradient(#e2e2e2,#f8f8f8);border:1px solid #cfcfcf}
.lang{left:784px;top:84px;width:95px;height:18px;border-radius:9px;background:#f3f3f3;border:1px solid #ccc;font-size:10px;color:#555;padding:2px 0 0 12px}
.lang::after{content:"";position:absolute;right:10px;top:7px;border:3px solid transparent;border-top:4px solid #666}
/* stats */
.card{background:var(--panel);border:1px solid #dcdcdc;border-radius:8px;box-shadow:0 1px 2px rgba(0,0,0,.08)}
.stats{left:80px;top:130px;width:195px;height:252px;padding:8px 12px 0 12px}
.stat{display:flex;align-items:center;gap:10px;height:32px;font-size:10.5px;border-bottom:1px dotted #bbb}
.stat:last-child{border-bottom:0}
/* video */
.video{left:289px;top:131px;width:395px;height:248px;background:#1c2226;border-radius:3px}
.video-frame{left:5px;top:5px;width:385px;height:197px;background:linear-gradient(160deg,#3f6fa8,#8cb1d6 45%,#c59a7c 60%,#2d4f7a)}
.play{left:168px;top:82px;width:52px;height:52px;border-radius:50%;background:radial-gradient(#eee,#aaa)}
.progress{left:7px;top:207px;width:378px;height:5px;border-radius:3px;background:#395a64}
.progress i{position:absolute;left:0;top:0;width:110px;height:5px;border-radius:3px;background:#3bb3d6}
.ctrl{height:18px;top:222px;border-radius:3px;background:#e6e6e6;font-size:7px;color:#666;text-align:center;line-height:18px}
/* login */
.tab{top:132px;height:21px;font-size:11px;line-height:21px;text-align:center}
.tab-on{left:716px;width:58px;background:var(--navy);color:#fff;border-radius:4px 4px 0 0}
.tab-off{left:782px;width:66px;color:#444}
.login{left:701px;top:153px;width:173px;height:228px;padding:26px 10px 0 10px;font-size:10.5px}
.login label{display:block;margin-left:5px}
.field{height:24px;border-radius:12px;border:1px solid #d0d0d0;background:#fff;margin:8px 0 16px}
.forgot{color:var(--navy);text-decoration:underline;font-size:9.5px;margin:-2px 0 0 8px;display:block}
.login-btn{position:absolute;left:101px;top:171px;width:60px;height:25px;border-radius:4px;background:linear-gradient(#2a64a6,var(--navy-dark));color:#fff;font-weight:700;font-size:12px;text-align:center;line-height:25px}
.save{position:absolute;left:17px;top:204px;font-size:9.5px;color:#555}
/* categories */
.cat{top:414px;width:137px;height:46px;border-radius:6px;background:linear-gradient(#2b69ad,var(--navy-dark));color:#fff;font-family:"Roboto Condensed",sans-serif;font-weight:700;font-size:16px;text-align:center;line-height:46px;box-shadow:0 2px 3px rgba(0,0,0,.25)}
/* projects */
.project{top:494px;width:186px;height:344px;background:#fbfbfb}
.project h2{position:absolute;left:23px;top:12px;font-family:"Roboto Condensed",sans-serif;font-weight:400;font-size:20px;color:#222}
.thumb{position:absolute;left:12px;top:50px;width:164px;height:90px;background:#d0d0d0;padding:6px}
.thumb div{width:100%;height:100%}
.blurb{position:absolute;left:10px;top:148px;width:166px;font-size:8.5px;line-height:14.5px;text-align:center;color:#444}
.bar{position:absolute;left:19px;top:208px;width:150px;height:14px;border-radius:7px;background:#fff;border:1px solid #ccc}
.bar span{position:absolute;right:-1px;top:-1px;width:68px;height:14px;border-radius:7px;background:#8a8a8a;color:#fff;font-size:8px;line-height:14px;text-align:center}
.amount{position:absolute;left:52px;top:236px;width:96px;height:18px;border-radius:3px;background:#c9c9c9;color:#fff;font-size:8px;line-height:18px;text-align:center}
.tag{position:absolute;top:266px;height:19px;border-radius:3px;color:#fff;font-size:7.5px;font-weight:700;line-height:19px;text-align:center;font-family:"Roboto Condensed",sans-serif}
.tag-blue{left:20px;width:60px;background:var(--navy)}
.tag-lime{left:115px;width:57px;background:linear-gradient(#bfdc3b,var(--lime-dark))}
.invest{position:absolute;left:36px;top:302px;width:112px;height:30px;border-radius:4px;background:linear-gradient(#2b69ad,var(--navy-dark));color:#fff;font-family:"Roboto Condensed",sans-serif;font-weight:700;font-size:15px;letter-spacing:.5px;text-align:center;line-height:30px}
/* view all */
.view-all{left:371px;top:883px;width:218px;height:93px;border-radius:4px;background:linear-gradient(#2361a5,var(--navy-dark));color:#fff;text-align:center;padding-top:13px}
.view-all strong{display:block;font-size:13px}
.view-all p{font-size:13px;margin-top:3px}
.yes{margin:8px auto 0;width:167px;height:27px;border-radius:4px;background:linear-gradient(#6cb2f2,#1c6fc9);font-weight:700;font-size:13px;line-height:27px}
/* footer */
.footer{left:0;top:1019px;width:960px;height:156px;background:linear-gradient(var(--footer-dark),var(--footer) 30%,var(--footer));border-top:1px solid #0f3563;color:#fff;font-family:Ubuntu,sans-serif}
.fcol{top:18px}
.fcol h3{font-weight:400;font-size:17px;margin-bottom:10px}
.fcol li{list-style:none;font-size:9.5px;line-height:16px;padding-left:12px;position:relative}
.fcol li::before{content:"";position:absolute;left:0;top:5px;border:3px solid transparent;border-left:4px solid #fff}
.contact p{font-size:9.5px;line-height:14.5px}
.social{top:32px;width:29px;height:29px}
.foot-brand{left:698px;top:110px;display:flex;align-items:center;gap:6px}
.foot-brand .brand-mark{background:#c9d3df}
.foot-brand .brand-name{color:#d7dde5}
.copy{left:0;top:1175px;width:960px;height:25px;background:#173e70;color:#fff;font-size:9px;line-height:25px;padding-left:94px}
</style>
</head>
<body>

<header class="abs header">
  <div class="abs brand"><span class="brand-mark"></span><span class="brand-name">HARVEST CELLAR</span></div>
  <div class="abs nav-btn" style="left:338px">How it Works ?</div>
  <div class="abs nav-btn" style="left:449px">Projects Review</div>
  <div class="abs nav-btn" style="left:561px">Virtual Office</div>
  <div class="abs search">
    <svg width="16" height="16" style="position:absolute;left:9px;top:7px"><circle cx="6" cy="6" r="4.5" fill="none" stroke="#333" stroke-width="1.6"/><line x1="9.5" y1="9.5" x2="14" y2="14" stroke="#333" stroke-width="2"/></svg>
  </div>
  <div class="abs lang">English</div>
</header>

<section class="abs card stats">
  <div class="stat"><svg width="12" height="12"><rect x=".5" y="1.5" width="10" height="10" fill="none" stroke="#333"/><path d="M2 6l3 3 6-8" fill="none" stroke="#333" stroke-width="1.8"/></svg>$ 50 000 000 of Investment</div>
  <div class="stat"><svg width="12" height="12"><rect x=".5" y="1.5" width="10" height="10" fill="none" stroke="#333"/><path d="M2 6l3 3 6-8" fill="none" stroke="#333" stroke-width="1.8"/></svg>1600 Starts- ups</div>
  <div class="stat"><svg width="12" height="12"><rect x=".5" y="1.5" width="10" height="10" fill="none" stroke="#333"/><path d="M2 6l3 3 6-8" fill="none" stroke="#333" stroke-width="1.8"/></svg>700 Orgnization</div>
  <div class="stat"><svg width="12" height="12"><rect x=".5" y="1.5" width="10" height="10" fill="none" stroke="#333"/><path d="M2 6l3 3 6-8" fill="none" stroke="#333" stroke-width="1.8"/></svg>10 000 Investors</div>
  <div class="stat"><svg width="12" height="12"><rect x=".5" y="1.5" width="10" height="10" fill="none" stroke="#333"/><path d="M2 6l3 3 6-8" fill="none" stroke="#333" stroke-width="1.8"/></svg>5000 Employees</div>
  <div class="stat"><svg width="12" height="12"><rect x=".5" y="1.5" width="10" height="10" fill="none" stroke="#333"/><path d="M2 6l3 3 6-8" fill="none" stroke="#333" stroke-width="1.8"/></svg>2000 Partners</div>
  <div class="stat"><svg width="12" height="12"><rect x=".5" y="1.5" width="10" height="10" fill="none" stroke="#333"/><path d="M2 6l3 3 6-8" fill="none" stroke="#333" stroke-width="1.8"/></svg>$ 10 000 000 of Profit</div>
</section>

<section class="abs video">
  <div class="abs video-frame" role="img" aria-label="Business handshake in front of city towers and blue sky"></div>
  <div class="abs play"><svg width="52" height="52"><path d="M21 16l16 10-16 10z" fill="#222"/></svg></div>
  <div class="abs progress"><i></i></div>
  <div class="abs ctrl" style="left:4px;width:22px">▶</div>
  <div class="abs ctrl" style="left:30px;width:56px">2:33 / 9:49</div>
  <div class="abs ctrl" style="left:90px;width:85px;text-align:left;padding-left:8px;color:#1e7fbf">◀) ▮▮▮▮▮▯▯▯▯</div>
  <div class="abs ctrl" style="left:293px;width:48px">SHARE ▾</div>
  <div class="abs ctrl" style="left:345px;width:22px">⤢</div>
  <div class="abs ctrl" style="left:371px;width:22px;background:#4cbde8;color:#fff">HD</div>
</section>

<div class="abs tab tab-on">Login</div>
<div class="abs tab tab-off">Registration</div>
<section class="abs card login">
  <label>Email or Phone</label>
  <div class="field"></div>
  <label>Password</label>
  <div class="field"></div>
  <a class="forgot">Forgot the Password ?</a>
  <div class="login-btn">Login</div>
  <div class="save">✔&nbsp; Save login</div>
</section>

<div class="abs cat" style="left:108px">Recommended</div>
<div class="abs cat" style="left:313px">Poular</div>
<div class="abs cat" style="left:513px">Most invesed</div>
<div class="abs cat" style="left:713px">New</div>

<article class="abs card project" style="left:88px">
  <h2>Project A</h2>
  <div class="thumb"><div role="img" aria-label="Silhouettes of business partners shaking hands over a world map" style="background:linear-gradient(120deg,#1d4f8a,#8fb8df)"></div></div>
  <p class="blurb">Lorem Ipsum is simply dummy text of the printing and typesetting industry. Lorem Ipsum has been</p>
  <div class="bar"><span>70% success</span></div>
  <div class="amount">$90 000 invested</div>
  <div class="tag tag-blue">200 Invertor</div><div class="tag tag-lime">23 Day Left</div>
  <div class="invest">Invest</div>
</article>
<article class="abs card project" style="left:287px">
  <h2>Project B</h2>
  <div class="thumb"><div role="img" aria-label="Metal cash box holding banknotes" style="background:linear-gradient(#e8e8e8,#9a9a9a)"></div></div>
  <p class="blurb">Lorem Ipsum is simply dummy text of the printing and typesetting industry. Lorem Ipsum has been</p>
  <div class="bar"><span>70% success</span></div>
  <div class="amount">$90 000 invested</div>
  <div class="tag tag-blue">200 Invertor</div><div class="tag tag-lime">23 Day Left</div>
  <div class="invest">Invest</div>
</article>
<article class="abs card project" style="left:489px">
  <h2>Project C</h2>
  <div class="thumb"><div role="img" aria-label="Padlock over a blue circuit board pattern" style="background:linear-gradient(135deg,#0b2e57,#1a6fb0)"></div></div>
  <p class="blurb">Lorem Ipsum is simply dummy text of the printing and typesetting industry. Lorem Ipsum has been</p>
  <div class="bar"><span>70% success</span></div>
  <div class="amount">$90 000 invested</div>
  <div class="tag tag-blue">200 Invertor</div><div class="tag tag-lime">23 Day Left</div>
  <div class="invest">Invest</div>
</article>
<article class="abs card project" style="left:688px">
  <h2>Project D</h2>
  <div class="thumb"><div role="img" aria-label="Trader raising arms in front of stock market screens" style="background:linear-gradient(#5b9fd8,#d9ecf7)"></div></div>
  <p class="blurb">Lorem Ipsum is simply dummy text of the printing and typesetting industry. Lorem Ipsum has been</p>
  <div class="bar"><span>70% success</span></div>
  <div class="amount">$90 000 invested</div>
  <div class="tag tag-blue">200 Invertor</div><div class="tag tag-lime">23 Day Left</div>
  <div class="invest">Invest</div>
</article>

<section class="abs view-all">
  <strong>View all projects ?</strong>
  <p>More then 1000 projects</p>
  <div class="yes">YES</div>
</section>

<footer class="abs footer">
  <div class="abs fcol" style="left:98px">
    <h3>Quick Links</h3>
    <ul><li>Marketing Tips</li><li>Search Optimisation</li><li>Social Media</li><li>Video Marketing</li><li>Business Cases</li></ul>
  </div>
  <div class="abs fcol" style="left:284px;top:22px">
    <h3>How it Works</h3>
    <ul><li>Marketing Tips</li><li>Search Optimisation</li><li>Social Media</li><li>Video Marketing</li><li>Business Cases</li></ul>
  </div>
  <div class="abs fcol contact" style="left:461px">
    <h3>Contact Us</h3>
    <p>Level 4, 12 Marlow Lane</p>
    <p>Eastbrook NSW 2099</p>
    <p>Australia</p>
    <p>Tel. +61 2 5550 1234</p>
    <p>Email. info@harvestcellar.example</p>
  </div>
  <div class="abs social" style="left:689px;background:#ef7a1a"></div>
  <div class="abs social" style="left:725px;background:#3b5a9a"></div>
  <div class="abs social" style="left:758px;background:#d0432f"></div>
  <div class="abs social" style="left:798px;background:#38a8e0"></div>
  <div class="abs foot-brand"><span class="brand-mark"></span><span class="brand-name">HARVEST CELLAR</span></div>
</footer>
<div class="abs copy">Copyright © 2012 Northfield Holdings, LLC. All rights reserved.</div>

</body>
</html>
```